Silicone product manufacturer needs name card

we are a silicone proudct manufacturer, need a name card.
Updates

Dear All, Pls use the following information for the name card. Miriam Lodge Marketing Manager Mobile : HK (852) 64390528 : CN (86) 13905172246 Tel : 852-23847615 Fax : 852-27316840 Rm705,7/F, Fook Lam Ind. Ctr., 24-26 Tai Po Rd., Sai Kung, HK China Office : Tel:86-796-82534917 Fax : 86-769-83162054 5-6/F, Min Tak Building, No. 47 QiaoLin Road, Shi Pai Kou Town, Dong Guan City, PRC China Factory Brovin Technology Ltd Pak Lun Technology Ltd Tai Wen Kei (F.S) Silicone Products Co. Ltd Vexamir Technology Ltd Slogan on the name card : We are your best Business Partner With ISO9001 / ISO14001 / TS16949 LOGO Any query, pls contact me at miriamlodge@quarvex-mail.net Thanks, miriam

Reason: Dear All, Still can't choose the right one. Thanks, Miriam

Reason: still not confirm

Reason: working on revision. thanks

Reason: revising the design with designer. thanks

Reason: revising with designer ! thanks

Industry/Entity Type

Manufacturer

```html
<!DOCTYPE html>
<html lang="en">
<head>
<meta charset="utf-8">
<title>Brovin Technology – Name Card Back</title>
<link rel="stylesheet" href="https://fonts.googleapis.com/css2?family=Questrial&display=swap">
<style>
  :root {
    --card-blue: #7ba7d8;
    --ink-white: #ffffff;
    --mark-soft: rgba(255, 255, 255, 0.55);
  }
  * { margin: 0; padding: 0; box-sizing: border-box; }
  html, body {
    width: 1200px;
    height: 791px;
    overflow: hidden;
    background: var(--card-blue);
  }
  .card-back {
    position: relative;
    width: 1200px;
    height: 791px;
    background: var(--card-blue);
    overflow: hidden;
    font-family: "Questrial", "Century Gothic", sans-serif;
    color: var(--ink-white);
  }
  .brand-graphic {
    position: absolute;
    left: 0;
    top: 0;
    width: 600px;
    height: 791px;
    background: radial-gradient(ellipse 70% 65% at 18% 50%, var(--mark-soft) 0%, rgba(255,255,255,0.25) 55%, rgba(255,255,255,0) 100%);
  }
  .contact-block {
    position: absolute;
    right: 36px;
    top: 378px;
    text-align: right;
  }
  .web-address {
    font-size: 56px;
    line-height: 1;
    letter-spacing: 0.5px;
  }
  .slogan {
    margin-top: 4px;
    font-size: 33px;
    line-height: 1.1;
  }
</style>
</head>
<body>
  <main class="card-back">
    <div class="brand-graphic" role="img" aria-label="Large white curved stripe brand graphic sweeping in from the left edge"></div>
    <div class="contact-block">
      <p class="web-address">www.quarvex-one.net</p>
      <p class="slogan">We are your best Business Partner</p>
    </div>
  </main>
</body>
</html>
```